依頼詳細
今ある幸せをメッセージとして書き、ご報告と共にお祈り頂きます。それ以外にも献歌などのサブ的なイベントのご案内を盛り込みたいと思います。
記載項目
詳細は添付資料をご確認願います。また、添付画像をご利用下さい。
サイズ
A4
ページ数
片面
希望イメージ
シンプル 複雑
単色 カラフル
暗い 明るい
日常 高級
遊び心 厳粛
未来的 伝統的
女性的 男性的
希望する色
納品ファイル
• イラストレーター形式 (.ai)
補足説明
アウトラインの有るもの、無いもの双方でお願い致します。添付画像は加工OKです。
■ 選んだ理由

選定にあたりましては弊社内でメイン画像枠の取り方(グラデーション/エッジ)で大きく選考しました。その結果、グラデーションが良いとの意見が過半数を超え、その中で更に投票方式によりhasuventoさんのご提案を選ばせて頂きました。慰霊そしてお客様へのメッセージが重要でありながら、サブイベントでは楽しさを感じさせ、行ってみたくなる。弊社が考えるコンセプトそのものでした。
また、度重なる修正依頼にも応じて頂けました事、本当に助かりました。

■ 提案者全員のお礼・コメント

皆様より本当に多くのご提案を頂きました事、この場をお借りし、御礼申し上げます。今回初めてポルメットへの依頼であり、ご提案頂けるのか不安がありましたが、ご応募頂いた皆様が当社のコンセプトをご理解・ご提案頂きました事また、その表現力、感謝の言葉しかありません。今後もお力を頂く機会があろうかと思いますし、是非、依頼をしたいと思います。その時にまたご提案頂く事が出来れば幸いです。

```html
<!DOCTYPE html>
<html lang="ja">
<head>
<meta charset="utf-8">
<title>キャンドル慰霊祭</title>
<link href="https://fonts.googleapis.com/css2?family=Noto+Sans+JP:wght@400;500;700&family=Noto+Serif+JP:wght@500;700;900&display=swap" rel="stylesheet">
<style>
:root{
  --night:#1f120b;
  --umber:#3b2416;
  --ember:#7a4a22;
  --gold:#c9a45c;
  --gold-light:#ead29a;
  --cream:#f6efdf;
  --ink:#3a2a1e;
  --crimson:#c0262d;
  --white:#ffffff;
}
*{margin:0;padding:0;box-sizing:border-box}
html,body{width:849px;height:1200px;overflow:hidden;background:var(--cream)}
.flyer{position:relative;width:849px;height:1200px;font-family:"Noto Sans JP",sans-serif;color:var(--ink);overflow:hidden}

.hero{position:absolute;left:0;top:0;width:849px;height:655px;
  background:radial-gradient(ellipse at 12% 30%,#8a5a2a 0%,rgba(60,36,22,0) 35%),
             radial-gradient(ellipse at 65% 75%,#7d8a4e 0%,#b85a6a 18%,rgba(40,24,14,0) 45%),
             linear-gradient(180deg,var(--night) 0%,var(--umber) 60%,#4a2e1b 100%)}
.hero-frame{position:absolute;left:14px;top:14px;width:821px;height:627px;border:1px solid var(--gold);opacity:.6}
.lead{position:absolute;top:22px;width:100%;text-align:center;color:var(--white);font-size:15px;letter-spacing:.08em}
.title{position:absolute;top:44px;width:100%;text-align:center;font-family:"Noto Serif JP",serif;font-weight:700;font-size:64px;color:var(--white);letter-spacing:.06em}
.ribbon{position:absolute;top:124px;left:340px;width:170px;height:30px;border-top:1px solid var(--gold);border-bottom:1px solid var(--gold);text-align:center;font-family:"Noto Serif JP",serif;font-size:16px;line-height:28px;color:var(--gold-light);font-style:normal}
.message{position:absolute;top:166px;left:280px;width:500px;text-align:center;color:var(--white);font-size:16px;line-height:23px;font-weight:500}

.notice-bar{position:absolute;left:0;top:655px;width:849px;height:46px;display:flex;align-items:center;
  background:linear-gradient(90deg,#6b4220 0%,var(--gold) 55%,var(--gold-light) 100%)}
.notice-bar .label{margin-left:40px;color:var(--white);font-family:"Noto Serif JP",serif;font-weight:700;font-size:22px}
.notice-bar .date{margin-left:auto;margin-right:40px;color:var(--umber);font-weight:700;font-size:19px}

.events{position:absolute;left:0;top:701px;width:849px;height:499px;background:var(--cream)}
.photo{position:absolute;border:2px solid var(--white);box-shadow:0 1px 3px rgba(0,0,0,.25)}
.photo-singer{left:40px;top:115px;width:118px;height:160px;background:linear-gradient(160deg,#d8c7a8,#a07a55)}
.photo-balloon{left:440px;top:22px;width:140px;height:110px;background:linear-gradient(150deg,#f2f2ef,#b9d4c8)}
.photo-bouquet{left:440px;top:150px;width:125px;height:110px;background:linear-gradient(150deg,#f0c2c7,#c9485a 60%,#6f8a3f)}

.event-head{position:absolute;font-family:"Noto Serif JP",serif;font-weight:900;font-size:22px;color:var(--crimson)}
.event-head::before{content:"";display:inline-block;width:10px;height:10px;background:var(--crimson);border-radius:50%;margin-right:6px;vertical-align:middle}
.song .event-head{left:40px;top:18px}
.song .times{position:absolute;left:40px;top:54px;font-size:15px;font-weight:700}
.song .performer{position:absolute;left:175px;top:80px;font-size:16px;font-weight:700}
.song .bio{position:absolute;left:175px;top:108px;width:240px;font-size:12px;line-height:19px}
.song .bio strong{color:var(--ember)}

.mall .event-head{left:598px;top:30px}
.mall .times{position:absolute;left:598px;top:68px;font-size:15px;font-weight:700;line-height:22px}
.gift{position:absolute;left:585px;top:178px;width:220px;font-family:"Noto Serif JP",serif;font-weight:700;font-size:18px;line-height:28px;color:var(--crimson)}

.notes{position:absolute;left:40px;top:305px;width:420px;list-style:none;font-size:12px;line-height:19px}
.notes li::before{content:"■";color:var(--ember);margin-right:4px}

.organizer{position:absolute;left:175px;top:395px;display:flex;align-items:center;gap:12px}
.organizer .mark{width:36px;height:36px;border-radius:50%;background:var(--gold)}
.organizer .name{font-size:15px;font-weight:700;color:var(--ink)}
.organizer .info{font-size:12px;line-height:18px}
.organizer .tel{display:flex;align-items:center;gap:4px}
</style>
</head>
<body>
<div class="flyer">
  <section class="hero" role="img" aria-label="キャンドルが灯る中、開かれたメッセージ帳と色とりどりの花で飾られた祭壇">
    <div class="hero-frame"></div>
    <p class="lead">1年に1度、遺族の方々が故人を偲ぶ日を催しています。</p>
    <h1 class="title">キャンドル慰霊祭</h1>
    <p class="ribbon">先だった方の願い</p>
    <p class="message">それは遺された家族が日々の生活を幸せにおくることではないでしょうか<br>いつも見守ってくれている大切な人へ<br>あの頃のこと、今日のこと、これからのこと<br>家族みんなの笑顔とともにメッセージとし、<br>お届けにいらっしゃいませんか</p>
  </section>

  <div class="notice-bar">
    <span class="label">キャンドル慰霊祭開催の御案内</span>
    <span class="date">2016年7月16日(土) 14:00~18:00</span>
  </div>

  <section class="events">
    <div class="song">
      <h2 class="event-head">献歌</h2>
      <p class="times">14:30~　16:00~</p>
      <p class="performer">森川 ゆり さん</p>
      <p class="bio"><strong>青葉市在住のシンガーソングライター</strong><br>温かな歌声で人の心に寄り添う楽曲を届け、地域の催しや式典で多くの方に親しまれています。大切な人への想いを歌に込めてお贈りします。</p>
      <div class="photo photo-singer" role="img" aria-label="ギターを抱えて歌う歌手の写真"></div>
    </div>

    <div class="mall">
      <div class="photo photo-balloon" role="img" aria-label="バルーンで作った白い犬の作品の写真"></div>
      <h2 class="event-head">モールアート</h2>
      <p class="times">16:00~<br>受付30名様</p>
      <div class="photo photo-bouquet" role="img" aria-label="プレゼント用の花束の写真"></div>
      <p class="gift">お花のプレゼントも<br>ございます。</p>
    </div>

    <ul class="notes">
      <li>すべて入場無料となっておりますので、ご家族ご友人をお誘いの上ご来場下さい。</li>
      <li>雨天の場合も会場内にて開催いたします。</li>
      <li>駐車場に限りがございますので、公共交通機関をご利用下さい。</li>
    </ul>

    <div class="organizer">
      <span class="mark"></span>
      <div>
        <p class="name">2016キャンドル慰霊祭事務局</p>
        <p class="info">青葉市水川町8-5</p>
        <p class="info tel">
          <svg width="12" height="12" viewBox="0 0 24 24" aria-hidden="true"><path fill="#3a2a1e" d="M6.6 10.8a15 15 0 0 0 6.6 6.6l2.2-2.2a1 1 0 0 1 1-.25 11.4 11.4 0 0 0 3.6.6 1 1 0 0 1 1 1V20a1 1 0 0 1-1 1A17 17 0 0 1 3 4a1 1 0 0 1 1-1h3.5a1 1 0 0 1 1 1c0 1.25.2 2.45.6 3.6a1 1 0 0 1-.25 1z"/></svg>
          0120-000-418
        </p>
      </div>
    </div>
  </section>
</div>
</body>
</html>
```